Business Card Design for a Technology Development Company

******* PLEASE NOTE (ALL DESIGNERS): I am going to finish the competition on Monday the 9th July (NOT SATURDAY 15TH). I have some designs I like and need to get them printed next week. Please submit any designs today or tomorrow. *******

PLEASE READ ALL OF THE REQUIREMENTS!!! I've rejected lot's of designs in the past because they didn't read the basic requirements - thanks and good luck!

Quill Harbor is a UK technology / small holding company that invests in startups and develops new ideas. In addition it provides IT Professional Services.

Ideally the design will be simple, professional, smart, and sophisticated, and overall be nice to look at. You can be creative as you like with the design, equally as simple as you like - you guys are the professionals so I'll leave it to your inspiration (make sure you incorporate the logo)!
Updates

PLEASE NOTE (ALL DESIGNERS): I am going to finish the competition on Monday the 9th July (NOT SATURDAY 15TH).  I have some designs I like and need to get them printed next week.  Please submit any designs today or tomorrow.

Target Market(s)

Enterprises / corporations / public sector / technical engineers / investors. More www.brontavex.com / www.pelmora.com than www.flinkaro.com!

Industry/Entity Type

Business

Requirements
Must have
• It should be modern and any artwork (if used) should be simple
- Pastel colours, dark and light colours, and shades are preferred over bright colours
- The design should incorporate the attached Quill Harbor logo and the logo colour scheme
- The logo should be on both sides. The back should just have the logo, maybe with some additional graphics
- It must have the following information on:

FirstName SecondName
Company Position
Email: name@quillharbor.co.uk
Mobile: +44 (0) 7700 900482

- The final design should be for a UK business card, dimensions: 85mm × 55mm
- The final design should have bleed marks to allow for printing and should be given in vector formats (EPS and AI)
Nice to have
• The Logo can be separated from the font in the logo on the front of the card. This isn't necessary or required, just to know it's not a limitation.
Should not have
• No bright colours (I prefer pastel colours, dark and light colours, and shades)
- Fonts that are to thin
- Effects or designs that make it difficult to print
- Italic or old fashioned looking fonts, i.e. anything like Times New Roman is a NO!

```html
<!DOCTYPE html>
<html lang="en">
<head>
<meta charset="utf-8">
<title>Quill Harbor – Business Card</title>
<link href="https://fonts.googleapis.com/css2?family=Source+Sans+3:wght@400;600&display=swap" rel="stylesheet">
<style>
  :root {
    --backdrop: #656665;
    --card-white: #ffffff;
    --brand-teal: #1e96ae;
    --brand-deep: #177a8a;
    --brand-sky: #7ecbea;
    --brand-mist: #e2f3f9;
    --ink: #3e4a4a;
  }
  html, body {
    margin: 0;
    padding: 0;
    width: 1200px;
    height: 900px;
    overflow: hidden;
    background: var(--backdrop);
    font-family: "Source Sans 3", "Myriad Pro", Arial, sans-serif;
  }
  .stage {
    position: relative;
    width: 1200px;
    height: 900px;
  }
  .card {
    position: absolute;
    left: 278px;
    width: 645px;
    height: 432px;
  }
  .card--front { top: 14px; background: var(--card-white); }
  .card--back  { top: 458px; background: var(--brand-teal); }

  .front-mark {
    position: absolute;
    left: 350px;
    top: 170px;
    width: 120px;
    height: 120px;
    border-radius: 50%;
    background: var(--brand-sky);
  }
  .divider {
    position: absolute;
    left: 244px;
    top: 90px;
    width: 3px;
    height: 252px;
    background: var(--brand-teal);
  }
  .contact {
    position: absolute;
    left: 290px;
    top: 124px;
    color: var(--ink);
  }
  .company-name {
    margin: 0 0 16px 4px;
    font-size: 36px;
    font-weight: 600;
    line-height: 1;
    color: var(--brand-deep);
  }
  .contact-line {
    margin: 0;
    font-size: 19px;
    line-height: 31px;
  }
  .contact-line--name { font-weight: 600; }

  .back-brand {
    position: absolute;
    inset: 0;
    display: flex;
    align-items: center;
    justify-content: center;
    gap: 20px;
  }
  .back-mark {
    width: 64px;
    height: 64px;
    border-radius: 50%;
    background: var(--brand-mist);
  }
  .back-name {
    margin: 0;
    font-size: 44px;
    font-weight: 600;
    color: var(--brand-mist);
  }
</style>
</head>
<body>
<main class="stage">
  <section class="card card--front" aria-label="Card front">
    <div class="front-mark" style="left:72px;top:136px;width:128px;height:128px;"></div>
    <div class="divider"></div>
    <div class="contact">
      <p class="company-name">Quill Harbor</p>
      <p class="contact-line contact-line--name">FirstName SecondName</p>
      <p class="contact-line">Company Position</p>
      <p class="contact-line">Email: name@quillharbor.co.uk</p>
      <p class="contact-line">Mobile: +44 (0) 7700 900482</p>
    </div>
  </section>

  <section class="card card--back" aria-label="Card back">
    <div class="back-brand">
      <span class="back-mark"></span>
      <p class="back-name">Quill Harbor</p>
    </div>
  </section>
</main>
</body>
</html>
```